KUVMA Powerpoint Template

A powerpoint template for our new brand of private label components which are built for us in Asia. We are looking for a fresh design for our powerpoint template. Note the subtle overlay of the fox in our theme. We like this as it implies quickness. Do not overuse the fox theme. It needs to be very subtle if used.

Our products include High performance passive RF and Fiber components and cable solutions for the wireless industry. Our comprehensive product portfolios include both general and low PIM grades and are widely used for cellular towers and in-building DAS systems as well as in the wireless research and development labs.

Common models include:
Filters
Diplexers, triplexers and 5plexers
Splitters and combiners
Signal tappers
Couplers
Terminations load and attenuators
Jumper cables and testing cables assemblies
Fiber Splice Trays
Patch Panels
Fiber Jumpers & Adapters

```html
<!DOCTYPE html>
<html lang="en">
<head>
<meta charset="utf-8">
<title>KUVMA Presentation Template</title>
<link href="https://fonts.googleapis.com/css2?family=Source+Sans+3:wght@300;400;600;900&display=swap" rel="stylesheet">
<style>
:root{
  --red:#e8221b;
  --black:#111111;
  --ink:#2a2a2a;
  --board:#e4e4e4;
  --paper:#ffffff;
  --rule:#d6d6d6;
  --ghost:rgba(225,225,225,.55);
}
*{margin:0;padding:0;box-sizing:border-box}
html,body{width:1200px;height:783px;overflow:hidden}
body{background:var(--board);font-family:"Source Sans 3",Arial,sans-serif;position:relative}
.slide{position:absolute;width:364px;height:229px;background:var(--paper);overflow:hidden;box-shadow:0 1px 3px rgba(0,0,0,.18)}
.c1{left:37px}.c2{left:420px}.c3{left:803px}
.r1{top:18px}.r2{top:273px}.r3{top:532px}
.backdrop-mark{position:absolute;left:-6px;bottom:-30px;font-weight:900;font-size:92px;letter-spacing:4px;color:var(--ghost);line-height:1;white-space:nowrap}
.brand{position:absolute;display:flex;align-items:center;gap:3px;font-weight:900;color:var(--black);line-height:1;letter-spacing:.5px}
.brand::before{content:"";width:.55em;height:.55em;background:var(--red)}
.brand.small{font-size:13px}
.brand.corner{right:10px;bottom:9px}
.page-no{position:absolute;left:50%;bottom:12px;width:6px;height:6px;margin-left:-3px;border:.6px solid var(--ink);border-radius:50%}
.copy{position:absolute;font-size:4.3px;line-height:7.4px;color:var(--ink)}
.copy p{margin-bottom:0}
.copy .accent{color:var(--red)}
.copy.wide{font-size:5px;line-height:7.8px}
.two-col{display:flex;gap:8px}
.two-col .col{flex:1}
.heading-plain{position:absolute;left:25px;top:25px;font-size:8px;color:var(--red);font-weight:400}
.heading-rule{position:absolute;left:25px;right:96px;top:39px;height:.6px;background:var(--rule)}
.bar{position:absolute;left:17px;top:20px;height:11px;display:flex;align-items:center}
.bar .label{font-size:7.5px;padding-left:7px;line-height:1}
.bar.dark{right:17px;background:var(--black)}
.bar.dark .label{color:var(--red)}
.bar.dark::after{content:"";position:absolute;right:0;top:0;width:7px;height:100%;background:var(--red)}
.bar.bright{right:17px;background:var(--red)}
.bar.bright .label{color:#fff}
.bar.bright::after{content:"";position:absolute;right:0;top:0;width:7px;height:100%;background:var(--black)}
.bar.partial{width:235px;background:var(--red)}
.bar.partial .label{color:#fff}
.end-block{position:absolute;right:17px;top:20px;width:12px;height:11px;background:var(--black)}
.top-strip{position:absolute;left:0;right:0;top:0;height:5px;background:var(--red)}
.hr{position:absolute;height:.6px;background:var(--rule)}
.cover-line{position:absolute;top:116px;height:1.4px}
.cover-title{position:absolute;left:184px;top:108px;font-size:13px;font-weight:300;color:var(--red);letter-spacing:.2px}
.cover-divider{position:absolute;left:165px;top:108px;width:.8px;height:15px;background:var(--ink)}
.v-rule{position:absolute;left:139px;top:25px;bottom:25px;width:.6px;background:var(--rule)}
</style>
</head>
<body>

<!-- Cover -->
<section class="slide c1 r1">
  <div class="backdrop-mark">KUVMA</div>
  <div class="cover-line" style="left:0;width:35px;background:var(--red)"></div>
  <div class="brand" style="left:72px;top:109px;font-size:14px">KUVMA</div>
  <div class="cover-divider"></div>
  <div class="cover-title">TITLE GOES HERE</div>
  <div class="cover-line" style="right:0;width:26px;background:var(--black)"></div>
</section>

<!-- Heading with rule -->
<section class="slide c2 r1">
  <div class="backdrop-mark">KUVMA</div>
  <div class="heading-plain">HEADING</div>
  <div class="heading-rule"></div>
  <div class="copy" style="left:25px;top:44px;width:256px">
    <p>Lorem ipsum dolor sit amet, consectetur adipisicing elit, sed do eiusmod tempor incididunt ut labore et dolore magna aliqua.</p>
    <p>Ut enim ad minim veniam, quis nostrud exercitation ullamco laboris nisi ut aliquip ex ea commodo consequat. Duis aute irure</p>
    <p>dolor in reprehenderit in voluptate velit esse cillum dolore eu fugiat nulla pariatur. Excepteur sint occaecat cupidatat non</p>
    <p>proident, sunt in culpa qui officia deserunt mollit anim id est laborum. Sed ut perspiciatis unde omnis iste natus error sit volup-</p>
    <p>tatem accusantium doloremque laudantium, totam rem aperiam, eaque ipsa quae ab illo inventore veritatis et quasi architecto</p>
    <p>beatae vitae dicta sunt explicabo. Nemo enim ipsam voluptatem quia voluptas sit aspernatur aut odit aut fugit,</p>
    <p>sed quia consequuntur magni dolores eos qui ratione voluptatem sequi nesciunt. Neque porro quisquam est, qui</p>
    <p>dolorem ipsum quia dolor sit amet, consectetur, adipisci velit, sed quia non numquam eius modi tempora</p>
    <p>incidunt ut labore et dolore magnam aliquam quaerat voluptatem.</p>
    <p>Nemo enim ipsam voluptatem quia voluptas sit aspernatur aut odit aut fugit,</p>
    <p>sed quia consequuntur magni dolores eos qui ratione voluptatem sequi nesciunt. Neque porro quisquam est, qui</p>
    <p>dolorem ipsum quia dolor sit amet, consectetur, adipisci velit, sed quia non numquam eius modi tempora</p>
    <p>incidunt ut labore et dolore magnam aliquam quaerat voluptatem eaque ipsa quae ab illo inventore veritatis et quasi archi-</p>
    <p>tecto beatae vitae dicta sunt explicabo.</p>
  </div>
  <div class="page-no"></div>
  <div class="brand small corner">KUVMA</div>
</section>

<!-- Dark bar, empty -->
<section class="slide c3 r1">
  <div class="backdrop-mark">KUVMA</div>
  <div class="bar dark"><span class="label">HEADING</span></div>
  <div class="page-no"></div>
  <div class="brand small corner">KUVMA</div>
</section>

<!-- Dark bar, two columns -->
<section class="slide c1 r2">
  <div class="backdrop-mark">KUVMA</div>
  <div class="bar dark"><span class="label">HEADING</span></div>
  <div class="copy two-col" style="left:17px;right:17px;top:36px">
    <div class="col">
      <p>Lorem ipsum dolor sit amet, consectetur adipisicing elit, sed do eiusmod tempor incididunt ut labore et dolore magna aliqua.</p>
      <p>Ut enim ad minim veniam, quis nostrud exercitation ullamco laboris nisi ut aliquip ex ea commodo consequat. Duis aute irure dolor in reprehenderit in voluptate velit esse cillum dolore eu fugiat nulla pariatur. Excepteur sint occaecat cupidatat non proident, sunt in culpa qui officia deserunt mollit anim id est laborum. Sed ut perspiciatis unde omnis iste natus error sit voluptatem accusantium doloremque laudantium, totam rem aperiam, eaque ipsa quae ab illo inventore veritatis et quasi architecto</p>
      <p>beatae vitae dicta sunt explicabo. Nemo enim ipsam voluptatem quia voluptas sit aspernatur aut odit aut fugit, sed quia consequuntur magni dolores eos qui ratione voluptatem sequi nesciunt. Neque porro quisquam est, qui dolorem ipsum quia dolor sit amet, consectetur, adipisci velit, sed quia non numquam eius modi tempora incidunt ut labore et dolore magnam aliquam quaerat voluptatem.</p>
      <p>Excepteur sint occaecat cupidatat non proident, sunt in culpa qui officia deserunt mollit anim id est laborum. Sed ut perspiciatis unde omnis iste natus error sit voluptatem accusantium doloremque laudantium, totam rem aperiam, eaque ipsa quae ab illo inventore veritatis et quasi architecto</p>
      <p>Duis aute irure dolor in reprehenderit in voluptate velit esse cillum dolore eu fugiat nulla pariatur.</p>
    </div>
    <div class="col">
      <p>Lorem ipsum dolor sit amet, consectetur adipisicing elit, sed do eiusmod tempor incididunt ut labore et dolore magna aliqua.</p>
      <p>Ut enim ad minim veniam, quis nostrud exercitation ullamco laboris nisi ut aliquip ex ea commodo consequat. Duis aute irure dolor in reprehenderit in voluptate velit esse cillum dolore eu fugiat nulla pariatur. Excepteur sint occaecat cupidatat non proident, sunt in culpa qui officia deserunt mollit anim id est laborum. Sed ut perspiciatis unde omnis iste natus error sit voluptatem accusantium doloremque laudantium, totam rem aperiam, eaque ipsa quae ab illo inventore veritatis et quasi architecto</p>
      <p>beatae vitae dicta sunt explicabo. Nemo enim ipsam voluptatem quia voluptas sit aspernatur aut odit aut fugit, sed quia consequuntur magni dolores eos qui ratione voluptatem sequi nesciunt. Neque porro quisquam est, qui dolorem ipsum quia dolor sit amet, consectetur, adipisci velit, sed quia non numquam eius modi tempora incidunt ut labore et dolore magnam aliquam quaerat voluptatem.</p>
      <p>Excepteur sint occaecat cupidatat non proident, sunt in culpa qui officia deserunt mollit anim id est laborum. Sed ut perspiciatis unde omnis iste natus error sit voluptatem accusantium doloremque laudantium, totam rem aperiam, eaque ipsa quae ab illo inventore veritatis et quasi architecto</p>
      <p>Duis aute irure dolor in reprehenderit in voluptate velit esse cillum dolore eu fugiat nulla pariatur.</p>
    </div>
  </div>
  <div class="page-no"></div>
  <div class="brand small corner">KUVMA</div>
</section>

<!-- Red bar, two columns with accent -->
<section class="slide c2 r2">
  <div class="backdrop-mark">KUVMA</div>
  <div class="bar bright"><span class="label">HEADING</span></div>
  <div class="copy two-col" style="left:17px;right:17px;top:36px">
    <div class="col">
      <p>Lorem ipsum dolor sit amet, consectetur adipisicing elit, sed do eiusmod tempor incididunt ut labore et dolore magna aliqua.</p>
      <p>Ut enim ad minim veniam, quis nostrud exercitation ullamco laboris nisi ut aliquip ex ea commodo consequat. Duis aute irure dolor in reprehenderit in voluptate velit esse cillum dolore eu fugiat nulla pariatur. Excepteur sint occaecat cupidatat non proident, sunt in culpa qui officia deserunt mollit anim id est laborum. Sed ut perspiciatis unde omnis iste natus error sit voluptatem accusantium doloremque laudantium, totam rem aperiam, eaque ipsa quae ab illo inventore veritatis et quasi architecto</p>
      <p>beatae vitae dicta sunt explicabo. Nemo enim ipsam voluptatem quia voluptas sit aspernatur aut odit aut fugit, sed quia consequuntur magni dolores eos qui ratione voluptatem sequi nesciunt. Neque porro quisquam est, qui dolorem ipsum quia dolor sit amet, consectetur, adipisci velit, sed quia non numquam eius modi tempora incidunt ut labore et dolore magnam aliquam quaerat voluptatem.</p>
      <p>Excepteur sint occaecat cupidatat non proident, sunt in culpa qui officia deserunt mollit anim id est laborum. Sed ut perspiciatis unde omnis iste natus error sit voluptatem accusantium doloremque laudantium, totam rem aperiam, eaque ipsa quae ab illo inventore veritatis et quasi architecto</p>
      <p>Duis aute irure dolor in reprehenderit in voluptate velit esse cillum dolore eu fugiat nulla pariatur.</p>
    </div>
    <div class="col">
      <p>Lorem ipsum dolor sit amet, consectetur adipisicing elit, sed do eiusmod tempor incididunt ut labore et dolore magna aliqua.</p>
      <p>Ut enim ad minim veniam, quis nostrud exercitation ullamco laboris nisi ut aliquip ex ea commodo consequat. Duis aute irure dolor in reprehenderit in voluptate velit esse cillum dolore eu fugiat nulla pariatur. Excepteur sint occaecat cupidatat non proident, sunt in culpa qui officia deserunt mollit anim id est laborum. Sed ut perspiciatis unde omnis iste natus error sit voluptatem accusantium doloremque laudantium, totam rem aperiam, eaque ipsa quae ab illo inventore veritatis et quasi architecto</p>
      <p class="accent">beatae vitae dicta sunt explicabo. Nemo enim ipsam voluptatem quia voluptas sit aspernatur aut odit aut fugit, sed quia consequuntur magni dolores eos qui ratione voluptatem sequi nesciunt. Neque porro quisquam est, qui dolorem ipsum quia dolor sit amet, consectetur, adipisci velit, sed quia non numquam eius modi tempora incidunt ut labore et dolore magnam aliquam quaerat voluptatem.</p>
      <p>Excepteur sint occaecat cupidatat non proident, sunt in culpa qui officia deserunt mollit anim id est laborum. Sed ut perspiciatis unde omnis iste natus error sit voluptatem accusantium doloremque laudantium, totam rem aperiam, eaque ipsa quae ab illo inventore veritatis et quasi architecto</p>
      <p>Duis aute irure dolor in reprehenderit in voluptate velit esse cillum dolore eu fugiat nulla pariatur.</p>
    </div>
  </div>
  <div class="page-no"></div>
  <div class="brand small corner">KUVMA</div>
</section>

<!-- Partial red bar with brand -->
<section class="slide c3 r2">
  <div class="backdrop-mark">KUVMA</div>
  <div class="bar partial"><span class="label">HEADING</span></div>
  <div class="brand small" style="left:258px;top:19px">KUVMA</div>
  <div class="end-block"></div>
  <div class="copy wide" style="left:25px;right:20px;top:49px">
    <p>Lorem ipsum dolor sit amet, consectetur adipisicing elit, sed do eiusmod tempor incididunt ut labore et dolore magna aliqua.</p>
    <p>Ut enim ad minim veniam, quis nostrud exercitation ullamco laboris nisi ut aliquip ex ea commodo consequat. Duis aute irure dolor in reprehende-rit in voluptate velit esse cillum dolore eu fugiat nulla pariatur. Excepteur sint occaecat cupidatat non proident, sunt in culpa qui officia deserunt mollit anim id est laborum. Sed ut perspiciatis unde omnis iste natus error sit voluptatem accusantium doloremque laudantium, totam rem aperiam, eaque ipsa quae ab illo inventore veritatis et quasi architecto</p>
    <p class="accent">beatae vitae dicta sunt explicabo. Nemo enim ipsam voluptatem quia voluptas sit aspernatur aut odit aut fugit, sed quia consequuntur magni dolores eos qui ratione voluptatem sequi nesciunt. Neque porro quisquam est, qui dolorem ipsum quia dolor sit amet, consectetur, adipisci velit, sed quia non numquam eius modi tempora incidunt ut labore et dolore magnam aliquam quaerat voluptatem.</p>
    <p>Excepteur sint occaecat cupidatat non proident, sunt in culpa qui officia deserunt mollit anim id est laborum. Sed ut perspiciatis unde omnis iste natus error sit voluptatem accusantium doloremque laudantium, totam rem aperiam, eaque ipsa quae ab illo inventore veritatis et quasi architecto</p>
    <p>Duis aute irure dolor in reprehenderit in voluptate velit esse cillum dolore eu fugiat nulla pariatur.</p>
  </div>
  <div class="hr" style="left:25px;right:20px;top:141px"></div>
  <div class="copy wide" style="left:25px;right:20px;top:145px">
    <p>Excepteur sint occaecat cupidatat non proident, sunt in culpa qui officia deserunt mollit anim id est laborum. Sed ut perspiciatis unde omnis iste natus error sit voluptatem accusantium doloremque laudantium, totam rem aperiam, eaque ipsa quae ab illo inventore veritatis et quasi archi-tecto</p>
  </div>
  <div class="page-no"></div>
</section>

<!-- Top strip, centred brand, text -->
<section class="slide c1 r3">
  <div class="backdrop-mark">KUVMA</div>
  <div class="top-strip"></div>
  <div class="brand small" style="left:155px;top:25px">KUVMA</div>
  <div class="copy wide" style="left:25px;right:20px;top:49px">
    <p>Lorem ipsum dolor sit amet, consectetur adipisicing elit, sed do eiusmod tempor incididunt ut labore et dolore magna aliqua.</p>
    <p>Ut enim ad minim veniam, quis nostrud exercitation ullamco laboris nisi ut aliquip ex ea commodo consequat. Duis aute irure dolor in reprehende-rit in voluptate velit esse cillum dolore eu fugiat nulla pariatur. Excepteur sint occaecat cupidatat non proident, sunt in culpa qui officia deserunt mollit anim id est laborum. Sed ut perspiciatis unde omnis iste natus error sit voluptatem accusantium doloremque laudantium, totam rem aperiam, eaque ipsa quae ab illo inventore veritatis et quasi architecto</p>
    <p class="accent">beatae vitae dicta sunt explicabo. Nemo enim ipsam voluptatem quia voluptas sit aspernatur aut odit aut fugit, sed quia consequuntur magni dolores eos qui ratione voluptatem sequi nesciunt. Neque porro quisquam est, qui dolorem ipsum quia dolor sit amet, consectetur, adipisci velit, sed quia non numquam eius modi tempora incidunt ut labore et dolore magnam aliquam quaerat voluptatem.</p>
    <p>Excepteur sint occaecat cupidatat non proident, sunt in culpa qui officia deserunt mollit anim id est laborum. Sed ut perspiciatis unde omnis iste natus error sit voluptatem accusantium doloremque laudantium, totam rem aperiam, eaque ipsa quae ab illo inventore veritatis et quasi architecto</p>
    <p>Duis aute irure dolor in reprehenderit in voluptate velit esse cillum dolore eu fugiat nulla pariatur.</p>
  </div>
  <div class="hr" style="left:25px;right:20px;top:144px"></div>
  <div class="copy wide" style="left:25px;right:20px;top:148px">
    <p>Excepteur sint occaecat cupidatat non proident, sunt in culpa qui officia deserunt mollit anim id est laborum. Sed ut perspiciatis unde omnis iste natus error sit voluptatem accusantium doloremque laudantium, totam rem aperiam, eaque ipsa quae ab illo inventore veritatis et quasi archi-tecto</p>
  </div>
  <div class="page-no"></div>
</section>

<!-- Top strip, centred brand, blank -->
<section class="slide c2 r3">
  <div class="backdrop-mark">KUVMA</div>
  <div class="top-strip"></div>
  <div class="brand small" style="left:155px;top:25px">KUVMA</div>
  <div class="hr" style="left:35px;right:35px;top:172px"></div>
  <div class="page-no"></div>
</section>

<!-- Top strip, brand left, text right -->
<section class="slide c3 r3">
  <div class="backdrop-mark">KUVMA</div>
  <div class="top-strip"></div>
  <div class="brand small" style="left:30px;top:113px">KUVMA</div>
  <div class="v-rule"></div>
  <div class="copy wide" style="left:158px;right:20px;top:30px">
    <p>Lorem ipsum dolor sit amet, consectetur adipisicing elit, sed do eiusmod tempor incididunt ut labore et dolore magna aliqua.</p>
    <p>Ut enim ad minim veniam, quis nostrud exercitation ullamco laboris nisi ut aliquip ex ea commodo consequat. Duis aute irure dolor in reprehenderit in voluptate velit esse cillum dolore eu fugiat nulla pariatur. Excepteur sint occaecat cupidatat non proident, sunt in culpa qui officia deserunt mollit anim id est laborum. Sed ut perspiciatis unde omnis iste natus error sit voluptatem accusantium doloremque laudantium, totam rem aperiam, eaque ipsa quae ab illo inventore veritatis et quasi architecto</p>
    <p class="accent">beatae vitae dicta sunt explicabo. Nemo enim ipsam voluptatem quia voluptas sit aspernatur aut odit aut fugit, sed quia consequuntur magni dolores eos qui ratione voluptatem sequi nesciunt. Neque porro quisquam est, qui dolorem ipsum quia dolor sit amet, consectetur, adipisci velit, sed quia non numquam eius modi tempora incidunt ut labore et dolore magnam aliquam quaerat voluptatem.</p>
    <p>Excepteur sint occaecat cupidatat non proident, sunt in culpa qui officia deserunt mollit anim id est laborum. Sed ut perspiciatis unde omnis iste natus error sit voluptatem accusantium doloremque laudantium, totam rem aperiam, eaque ipsa quae ab illo inventore veritatis et quasi architecto</p>
    <p>Duis aute irure dolor in reprehenderit in voluptate velit esse cillum dolore eu fugiat nulla pariatur.</p>
  </div>
  <div class="page-no"></div>
</section>

</body>
</html>
```